Property inventory reports of the highest quality for agents

We need a brochure for a residential inventory company providing condition reports at the start and end of tenancy for letting agents and private landlords for our company called Larkfield Reports. Our main target market is high end properties but we do work across the entire portfolio of properties available.

The main services we offer are:

1) Inventory compilation
2) Tenant check in
3) Tenant check out

This brochure should be designed to market to the Agent market alone, we will convert the final brochure to a version for other markets.

Final print ready specification to be confirmed shortly but will be A4 folded 297mm x 210mm and A3 unfolded 420mm x 297 mm with probably a .25inch bleed

Themes to communicate:

1) Quality and detailed reports
2) Easy to use and time saving reports
3) Top quality existing clients and testimonials (see website)
4) Professional and trust worthy
5) Accommodating and flexible

Main objectives of brochure:

1) Addition point of reference for sales messages across other media
2) Convert leads from conferences and booked meetings
3) Convert leads from booked meetings to instructions
4) Encouraging agents to call office number to book meeting or instruction
5) Outline services offered

Target Market(s)

Letting Agents, mainly high end but should appeal to all

Industry/Entity Type

Residential

Requirements
Must have
• 1) Use existing colours and typography from example brochures and corporate material
2) Pictures on exterior and interior pages mainly of quality property interiors
3) Main selling point should be included on cover and interior ‘Saving you time and reducing disputes’
4) Clear and prominent call to action for target market to call and book meeting or instructions

```html
<!DOCTYPE html>
<html lang="en">
<head>
<meta charset="utf-8">
<title>Larkfield Reports – Brochure Spread</title>
<link href="https://fonts.googleapis.com/css2?family=Source+Sans+3:wght@300;400;600;700&display=swap" rel="stylesheet">
<style>
:root{
  --backdrop:#1f1f21;
  --page:#ececec;
  --panel:#e4e4e4;
  --panel-dark:#cfcfcf;
  --ink:#1b1b1b;
  --muted:#4a4a4a;
  --soft:#8a8a8a;
  --sky:#7fb0de;
  --sky-light:#b9d5ee;
  --brand:#1f56b3;
  --brand-dark:#163f8c;
  --slate:#8d8f93;
  --white:#ffffff;
  --leaf:#b6d34a;
  --leaf-dark:#8fb02e;
}
*{margin:0;padding:0;box-sizing:border-box}
html,body{width:1200px;height:793px;overflow:hidden;background:var(--backdrop)}
body{font-family:"Source Sans 3",Arial,sans-serif;color:var(--ink);position:relative}
.spread{position:absolute;left:88px;top:57px;width:994px;height:703px;background:var(--page);box-shadow:0 6px 24px rgba(0,0,0,.55)}
.page-left{position:absolute;left:0;top:0;width:662px;height:651px}
.hero-photo{position:absolute;inset:0;background:linear-gradient(180deg,#f6f6f6 0%,#e9ecef 40%,#dfe3e6 62%,#8a5a3c 80%,#5e3420 100%)}
.intro-panel{position:absolute;left:22px;top:25px;width:273px;height:600px;background:rgba(255,255,255,.72);padding:10px 12px}
.intro-panel h1{font-weight:300;font-size:34px;line-height:34px;letter-spacing:.5px;color:var(--ink);margin-bottom:4px}
.intro-panel p{font-size:8.2px;line-height:11px;color:var(--muted);margin-bottom:9px}
.intro-panel p strong{color:var(--ink);font-weight:700}
.intro-panel h2{font-weight:300;font-size:34px;line-height:34px;margin:12px 0 6px}
.lead{font-size:11.5px!important;line-height:14px!important;color:var(--muted)!important;text-transform:uppercase;font-weight:300;margin-bottom:14px!important}
.core-services{list-style:none;font-weight:700;font-size:12px;line-height:15px;margin-bottom:12px}
.extra-intro{font-size:12px!important;line-height:14px!important;color:var(--muted)!important;margin-bottom:14px!important}
.extra-services{list-style:none;font-weight:700;font-size:9px;line-height:12px;margin-bottom:10px}
.page-right{position:absolute;left:662px;top:0;width:332px;height:651px;background:var(--page)}
.fold{position:absolute;left:662px;top:0;width:14px;height:651px;background:linear-gradient(90deg,rgba(0,0,0,.12),rgba(0,0,0,0))}
.service{position:absolute;left:8px;width:324px;background:linear-gradient(180deg,var(--panel) 0%,var(--panel-dark) 100%)}
.service h3{height:29px;padding-left:16px;font-size:17px;font-weight:600;color:var(--white);line-height:29px;background:linear-gradient(90deg,var(--sky) 0%,var(--sky-light) 60%,var(--sky) 100%)}
.service-body{display:flex;padding:11px 12px 0 12px;gap:12px}
.service-body ul{list-style:none;width:132px;font-size:9px;font-weight:700;line-height:13px}
.service-body ul li{padding-left:5px;text-indent:-5px}
.service-body p{width:152px;font-size:9px;line-height:12.2px;color:var(--ink)}
.compilation{top:0;height:135px}
.compilation h3{height:39px;line-height:49px}
.check-in{top:143px;height:125px}
.check-out{top:275px;height:125px}
.areas{position:absolute;left:8px;top:413px;width:324px;height:225px;background:linear-gradient(180deg,#ffffff 0%,#d9d9d9 100%)}
.areas h3{height:27px;padding-left:14px;background:var(--slate);color:var(--white);font-weight:300;font-size:23px;line-height:28px}
.coverage-map{position:absolute;left:14px;top:40px;width:290px;height:135px;border-radius:30px 60px 20px 40px;background:linear-gradient(135deg,var(--leaf) 0%,var(--leaf-dark) 100%)}
.areas .note{position:absolute;left:16px;top:184px;width:290px;font-size:8.4px;line-height:12px;color:var(--soft)}
.footer-band{position:absolute;left:0;top:651px;width:994px;height:52px;background:linear-gradient(180deg,var(--brand) 0%,var(--brand-dark) 100%)}
.site-url{position:absolute;left:189px;top:17px;color:var(--white);font-size:12.5px}
.brand{position:absolute;left:660px;top:14px;display:flex;align-items:center;gap:7px;color:var(--white);font-weight:700;font-size:16px;letter-spacing:.3px}
.brand-dot{width:10px;height:10px;border-radius:50%;background:var(--white)}
</style>
</head>
<body>
<main class="spread">
  <section class="page-left">
    <div class="hero-photo" role="img" aria-label="Bright empty penthouse interior with wooden floor and large windows, three people crouching to review a floor plan"></div>
    <article class="intro-panel">
      <h1>ABOUT US</h1>
      <p><strong>LARKFIELD REPORTS IS ONE OF THE LEADING INVENTORY COMPANIES</strong> and currently work with a large number of High Street Letting Agencies along and with an extensive number of Private Landlords across the Southeast of England.</p>
      <p><strong>WE HAVE GROWN MAINLY</strong> thanks to recommendation by our existing clients and the strength of the relationships we have formed with them. Vision is essential and we aim to become the only educated choice for all agents and landlords when selecting an inventory provider.</p>
      <p><strong>WORKING CLOSELY WITH CLIENTS</strong> means we keep up to date with their needs at all times to ensure we offer the best possible service. Our philosophy of constantly monitoring and updating the service offered to our clients and improving every detail of the systems we use to provide you with the best possible service available.</p>
      <h2>SERVICES</h2>
      <p class="lead">Larkfield Reports can provide the following basic services which will normally be the essential aspects of any tenancy:</p>
      <ul class="core-services">
        <li>- Inventory Compilation</li>
        <li>- Check In</li>
        <li>- Check Out</li>
      </ul>
      <p class="extra-intro">Additionally we provide a number of other services which may be of interest to certain clients depending on their needs and situation.</p>
      <ul class="extra-services">
        <li>- Snagging or mid tenancy inspections</li>
        <li>- Relocation inventories</li>
        <li>- Commercial inventories</li>
      </ul>
      <p>We have in the past also provided customised services including training, deposit workshops and industry event presenting so if there is a specific need you have please always get in touch.</p>
    </article>
  </section>

  <section class="page-right">
    <div class="service compilation">
      <h3>COMPILATION</h3>
      <div class="service-body">
        <ul><li>- Preparing Property</li><li>- Cleaning and Maintenance</li><li>- Assist in moving</li><li>- Best possible record</li></ul>
        <p>The inventory compilation is the initial appointment where we will attend to dictate the description and condition of the property, in most circumstances a few days before the start of the first tenancy.</p>
      </div>
    </div>
    <div class="service check-in">
      <h3>Check IN</h3>
      <div class="service-body">
        <ul><li>- Informing you of issues</li><li>- All aspects covered in move</li><li>- Keys &amp; Meter reading</li><li>- Everything agreed with you</li></ul>
        <p>All reports are produced and distributed promptly in digital format so they can be used easily throughout the tenancy to assist with any issues.</p>
      </div>
    </div>
    <div class="service check-out">
      <h3>Check OUT</h3>
      <div class="service-body">
        <ul><li>- Comprehensive report</li><li>- Fully attributed responsibilities</li><li>- Transparent &amp; clear format</li><li>- Info &amp; utilities obtained</li></ul>
        <p>Potentially the most important appointment is the Check Out and this is really where the Larkfield Reports service and report will provide you with maximum value.</p>
      </div>
    </div>
    <div class="areas">
      <h3>AREAS COVERED</h3>
      <div class="coverage-map" role="img" aria-label="Map of South East England counties covered: London, Berkshire, Surrey, Kent, Hampshire, West Sussex and East Sussex"></div>
      <p class="note">Should you require coverage in an area not listed above please contact us to discuss your requirements and we will do our best to accommodate your needs.</p>
    </div>
  </section>
  <div class="fold"></div>

  <footer class="footer-band">
    <span class="site-url">www.larkfieldreports.info</span>
    <div class="brand"><span class="brand-dot"></span>LARKFIELD REPORTS</div>
  </footer>
</main>
</body>
</html>
```